Business Card & Stationary Design Project

We are looking for some creative direction for business cards and our stationary.

We are a global logistics firm that has recently changed its name to Marrick Global Logistics and we have a new website due out tomorrow (www.marrick.com.au).

The colours of the company are rich navy tones, I would like to have business cards that fit together to make one picture on the back (possibly an old map of the world??), and the front to be modern contemporary looking.

But I am open to suggestions, so just incorporate our new logo and get going!
Updates

Hi Everyone,

Thank you for all of your designs so far and the time you have put into it.

I have asked many of you for amendments to see if we can get a final product, so with this in mind I am extending the deadline by a few days.

Good luck and thank you once again.

Please message me direct if you need any clarification.

Kind Regards
Colin

Reason: As outlined the extra 3 days is for amendments and changes to the current submissions. Thanks Colin

Industry/Entity Type

Business

```html
<!DOCTYPE html>
<html lang="en">
<head>
<meta charset="utf-8">
<title>Marrick Global Logistics – Business Card</title>
<link rel="stylesheet" href="https://fonts.googleapis.com/css2?family=Cinzel:wght@500&family=Exo+2:wght@300&display=swap">
<style>
  :root {
    --navy-deep: #0e2855;
    --navy-mid: #1a4384;
    --navy-light: #2456a0;
    --globe-light: #cfe6fb;
    --globe-mid: #4a8fd6;
    --globe-dark: #123c7e;
    --contact-blue: #2ea3e6;
    --logo-white: #ffffff;
    --page-bg: #ffffff;
  }
  * { margin: 0; padding: 0; box-sizing: border-box; }
  html, body {
    width: 1200px;
    height: 686px;
    overflow: hidden;
    background: var(--page-bg);
  }
  .business-card {
    position: relative;
    width: 1200px;
    height: 686px;
    border-radius: 30px;
    overflow: hidden;
    background: radial-gradient(ellipse 70% 80% at 35% 50%, var(--navy-light) 0%, var(--navy-mid) 45%, var(--navy-deep) 100%);
  }
  .globe-artwork {
    position: absolute;
    left: 648px;
    top: 24px;
    width: 712px;
    height: 712px;
  }
  .wordmark {
    position: absolute;
    left: 28px;
    top: 22px;
    color: var(--logo-white);
    font-family: "Cinzel", "Times New Roman", serif;
    font-weight: 500;
    white-space: nowrap;
  }
  .wordmark-name {
    display: block;
    font-size: 78px;
    line-height: 1;
    letter-spacing: 0.40em;
  }
  .wordmark-tagline {
    display: block;
    margin-top: 14px;
    font-size: 29px;
    line-height: 1;
    letter-spacing: 0.36em;
  }
  .contact-list {
    position: absolute;
    left: 20px;
    top: 208px;
    list-style: none;
    font-family: "Exo 2", "Helvetica Neue", Arial, sans-serif;
    font-weight: 300;
    font-size: 40px;
    color: var(--contact-blue);
  }
  .contact-item {
    display: flex;
    align-items: center;
    height: 57.5px;
    white-space: nowrap;
  }
  .contact-item.address-continued { padding-left: 52px; }
  .contact-icon {
    width: 42px;
    height: 42px;
    margin-right: 10px;
    flex-shrink: 0;
    fill: var(--logo-white);
  }
</style>
</head>
<body>
<div class="business-card">
  <svg class="globe-artwork" viewBox="0 0 712 712" role="img" aria-label="Illustrated globe showing Asia and Australia">
    <defs>
      <radialGradient id="globeShade" cx="0.42" cy="0.3" r="0.7">
        <stop offset="0" stop-color="var(--globe-light)"/>
        <stop offset="0.35" stop-color="var(--globe-mid)"/>
        <stop offset="1" stop-color="var(--globe-dark)"/>
      </radialGradient>
    </defs>
    <circle cx="356" cy="356" r="356" fill="url(#globeShade)"/>
  </svg>

  <div class="wordmark" aria-label="Marrick Global Logistics">
    <span class="wordmark-name">MARRICK</span>
    <span class="wordmark-tagline">GLOBAL LOGISTICS</span>
  </div>

  <ul class="contact-list">
    <li class="contact-item">
      <svg class="contact-icon" viewBox="0 0 24 24" aria-hidden="true"><path d="M12 3 1.5 11.5h3V21h6v-6h3v6h6v-9.5h3z"/></svg>
      87 Wattlebank Street
    </li>
    <li class="contact-item address-continued">Ultimo NSW 2007</li>
    <li class="contact-item">
      <svg class="contact-icon" viewBox="0 0 24 24" aria-hidden="true"><path d="M2 8c0-2 4-4 10-4s10 2 10 4v2h-5V8.5c-1.5-.5-3-.7-5-.7s-3.5.2-5 .7V10H2z"/><path d="M6 12h12l2 8H4z"/></svg>
      02 5550 1234
    </li>
    <li class="contact-item">
      <svg class="contact-icon" viewBox="0 0 24 24" aria-hidden="true"><path d="M7 1.5h10a1.5 1.5 0 0 1 1.5 1.5v18a1.5 1.5 0 0 1-1.5 1.5H7A1.5 1.5 0 0 1 5.5 21V3A1.5 1.5 0 0 1 7 1.5zm.5 2.5v6h9V4zm.5 8v2h2v-2zm3 0v2h2v-2zm3 0v2h2v-2zm-6 3v2h2v-2zm3 0v2h2v-2zm3 0v2h2v-2zm-6 3v2h2v-2zm3 0v2h2v-2zm3 0v2h2v-2z"/></svg>
      0400555018
    </li>
    <li class="contact-item">
      <svg class="contact-icon" viewBox="0 0 24 24" aria-hidden="true"><path d="M6 2h10l3 3v5H6zM3 11h18v8H3zm3 7h12v4H6z"/></svg>
      029555 7142
    </li>
    <li class="contact-item">
      <svg class="contact-icon" viewBox="0 0 24 24" aria-hidden="true"><path d="M2 5h20v14H2zm1.8 1.5 8.2 7 8.2-7z"/></svg>
      colin@marrick.com.au
    </li>
    <li class="contact-item">
      <svg class="contact-icon" viewBox="0 0 24 24" aria-hidden="true"><path fill-rule="evenodd" d="M12 2a10 10 0 1 1 0 20 10 10 0 0 1 0-20zm-1 1.6c-1.5 1.5-2.4 3.8-2.6 6.4H11zm2 0V10h2.6c-.2-2.6-1.1-4.9-2.6-6.4zM4 10h2.4c.1-2.2.7-4.2 1.7-5.7A8 8 0 0 0 4 10zm13.6 0H20a8 8 0 0 0-4.1-5.7c1 1.5 1.6 3.5 1.7 5.7zM4 12a8 8 0 0 0 4.1 7.7c-1-1.5-1.6-3.5-1.7-5.7H4.2zm4.4 0c.2 2.6 1.1 4.9 2.6 6.4V12zm4.6 0v6.4c1.5-1.5 2.4-3.8 2.6-6.4zm4.6 0c-.1 2.2-.7 4.2-1.7 5.7A8 8 0 0 0 19.8 12z"/></svg>
      marrick.com.au
    </li>
  </ul>
</div>
</body>
</html>
```